Offshore Energy Projects Management Consultancy needs a business card design

Logo available. We provide teams to deliver engineering consultancy, project management and delivery teams mainly in the offshore renewables sector. The company is all about bringing the right people to a project to deliver the scope.

The business card will be used for all staff.

The business card should be quite simple, vibrant and uncluttered but convey experience, enthusiasm and integration.

Target Market(s)

Energy Project Developers and Tier 1 construction companies

Contact Information for Business Card

Logo should be on the back of the card. I'm happy for the designer to play with the colour of the logo and background colour.

Front of the card should convey all the must have information in a clear and professional manner but without being overly traditional.

Colors

Designer to choose colors to be used in the design.

Requirements
Must have
• Land Line Tel Number, Mobile Tel Number, Email, business address, web address.

```html
<!DOCTYPE html>
<html lang="en">
<head>
<meta charset="utf-8">
<title>Northreach Delivery Group – Business Card</title>
<link rel="stylesheet" href="https://fonts.googleapis.com/css2?family=Open+Sans:wght@400;600;700&display=swap">
<style>
  :root {
    --blue: #0f76bf;
    --blue-light: #29a3dc;
    --ink: #4a4d52;
    --white: #ffffff;
    --paper: #f7f8f9;
    --backdrop: #c9cccf;
  }
  * { box-sizing: border-box; margin: 0; padding: 0; }
  html, body { width: 1200px; height: 800px; overflow: hidden; }
  body {
    background: var(--backdrop);
    font-family: "Open Sans", sans-serif;
    display: flex;
    align-items: center;
    justify-content: center;
    gap: 40px;
  }
  .card {
    position: relative;
    width: 540px;
    height: 309px;
    overflow: hidden;
    box-shadow: 0 6px 18px rgba(0,0,0,0.18);
  }

  /* Back of card */
  .card-back {
    background: var(--blue);
    color: var(--white);
    display: flex;
    flex-direction: column;
    align-items: center;
    justify-content: center;
  }
  .card-back .brand {
    display: flex;
    align-items: center;
    gap: 12px;
    margin-top: -20px;
  }
  .card-back .brand-mark {
    width: 18px; height: 18px;
    border-radius: 50%;
    background: var(--white);
  }
  .card-back .brand-name {
    font-size: 26px;
    font-weight: 700;
    letter-spacing: 0.5px;
    text-transform: uppercase;
    color: var(--white);
  }
  .card-back .web {
    position: absolute;
    bottom: 58px;
    left: 0; right: 0;
    text-align: center;
    font-size: 15px;
    letter-spacing: 2.5px;
  }

  /* Front of card */
  .card-front {
    background: linear-gradient(180deg, var(--white) 0%, var(--paper) 100%);
    color: var(--ink);
  }
  .card-front .brand {
    position: absolute;
    top: 30px; left: 34px;
    display: flex;
    align-items: center;
    gap: 9px;
  }
  .card-front .brand-mark {
    width: 13px; height: 13px;
    border-radius: 50%;
    background: var(--blue);
  }
  .card-front .brand-name {
    font-size: 18px;
    font-weight: 700;
    text-transform: uppercase;
    color: var(--blue);
    letter-spacing: 0.3px;
  }
  .contact {
    position: absolute;
    left: 34px;
    top: 104px;
    font-size: 13.5px;
    line-height: 20px;
    list-style: none;
  }
  .contact li { display: flex; align-items: center; gap: 7px; }
  .contact svg { width: 13px; height: 13px; flex: none; fill: none; stroke: var(--blue); stroke-width: 1.6; }
  .contact .icon-phone { fill: var(--blue); stroke: none; }
  .person {
    position: absolute;
    right: 40px;
    top: 134px;
    text-align: right;
  }
  .person .name {
    font-size: 19px;
    font-weight: 700;
    color: var(--blue);
  }
  .person .role {
    font-size: 14px;
    color: var(--blue-light);
  }
  .wave {
    position: absolute;
    left: 0; bottom: 0;
    width: 540px; height: 100px;
  }
  .card-front .web {
    position: absolute;
    right: 40px;
    bottom: 10px;
    font-size: 14px;
    letter-spacing: 2.5px;
    color: var(--white);
  }
</style>
</head>
<body>

  <section class="card card-back" aria-label="Back of business card">
    <div class="brand">
      <span class="brand-mark"></span>
      <span class="brand-name">Northreach Delivery Group</span>
    </div>
    <p class="web">www.ndg.ltd</p>
  </section>

  <section class="card card-front" aria-label="Front of business card">
    <div class="brand">
      <span class="brand-mark"></span>
      <span class="brand-name">Northreach Delivery Group</span>
    </div>

    <ul class="contact">
      <li>The Harbourline Building</li>
      <li>212 Quay Road, Portlethen, AB12 4QP</li>
      <li>
        <svg viewBox="0 0 14 14" aria-hidden="true"><rect x="3.5" y="1" width="7" height="12" rx="1.2"/><line x1="6" y1="11" x2="8" y2="11"/></svg>
        +44 1234 567 890
      </li>
      <li>
        <svg class="icon-phone" viewBox="0 0 14 14" aria-hidden="true"><path d="M3 1l2.2 2.6-1.2 1.6c.8 1.8 2.1 3.1 3.9 3.9l1.6-1.2L12 10.1 10.7 12.6C6 12.4 1.6 8 1.4 3.3z"/></svg>
        +44 1234 567 890
      </li>
      <li>
        <svg viewBox="0 0 14 14" aria-hidden="true"><rect x="1" y="3" width="12" height="8"/><polyline points="1,3 7,8 13,3"/></svg>
        martin@ndg.ltd
      </li>
    </ul>

    <div class="person">
      <p class="name">Martin Halloway</p>
      <p class="role">Director</p>
    </div>

    <svg class="wave" viewBox="0 0 540 100" preserveAspectRatio="none" aria-hidden="true">
      <path d="M0 24 C180 2 360 10 540 50 L540 100 L0 100 Z" fill="var(--blue-light)"/>
      <path d="M0 31 C180 10 360 18 540 56 L540 100 L0 100 Z" fill="var(--white)"/>
      <path d="M0 34 C180 14 360 22 540 60 L540 100 L0 100 Z" fill="var(--blue)"/>
    </svg>
    <p class="web">www.ndg.ltd</p>
  </section>

</body>
</html>
```